Plakate für Anbieter von Karosserie-Reparaturen und -Services
Zielgruppe
Unser Kunde, die Lindauer & Brack AG aus Oberbuchsiten (CH), ist ein Anbieter von Karosserie Reparaturen und Services. Er wird an einem öffentlichen Event teilnehmen und benötigt hierfür ein Plakat um seine Aktivität auf seinem Stand zu bewerben. Diese Aktivität ist für die Besucher die Teilnahme als Fahrer auf der Velotta-Rennbahn auf dem Stand. Hierfür benötigen wir ein Plakat (Format A0, farbig) welches auf das Rennen und die zu gewinneneden Preise aufmerksam macht.
Aufgabenstellung
Das Plakat muss modern, ansprechend, einladend und motivierend sein. Es kann mit Bilder (Vorschläge aus Lumexa-Stock) und Farben gearbeiten werden. Die Farben müssen nicht zwingend einen direkten Bezug zum Logo haben.
Dieser Text muss zwingend ersichtlich sein:
→ 15 Runden sind zu fahren
→ die schnellste Zeit gewinnt
Zu gewinnen gibt es
1. Preis: Gutschein im Wert von CHF 1'000.- von Vandermark
2. Preis: Fahrzeugreinigung inkl. Politur im Wert von CHF 800.-
3. Preis Werkstatt-Gutschein im Wert von CHF 400.-
Nebst dem Text benötigt es noch einen 'Call to Action' > z.B. Jetzt mitmachen und gewinne oder so ähnlich. Zudem benötigst es noch einen Platzhalter für ein zweites Logo. Dieses ist aktuell noch nicht definiert und wird dann erst bei der Finalisierung eingefügt.

```html
<!DOCTYPE html>
<html lang="de">
<head>
<meta charset="utf-8">
<title>15 Runden – Lindauer & Brack AG</title>
<link href="https://fonts.googleapis.com/css2?family=Anton&family=Montserrat:wght@500;600;700;800&display=swap" rel="stylesheet">
<style>
  :root {
    --page-bg: #e4e4e6;
    --brand-blue: #1f5fae;
    --race-orange: #e85a10;
    --race-yellow: #f7cd32;
    --teal: #14b3bd;
    --teal-deep: #0a3f48;
    --teal-dark: #06333b;
    --teal-bottom: #0c6e78;
    --white: #ffffff;
    --ink: #0d0d0d;
  }
  * { margin: 0; padding: 0; box-sizing: border-box; }
  html, body { width: 1200px; height: 1117px; overflow: hidden; background: var(--page-bg); }
  .poster {
    position: absolute; left: 230px; top: 22px; width: 740px; height: 1072px;
    overflow: hidden;
    background: linear-gradient(180deg, var(--teal-deep) 0%, var(--teal-dark) 75%, var(--teal-bottom) 100%);
    font-family: "Montserrat", sans-serif; color: var(--white);
  }
  .track-photo {
    position: absolute; left: 0; top: 0; width: 740px; height: 700px;
    background:
      linear-gradient(180deg, rgba(6,51,59,0) 82%, var(--teal-deep) 100%),
      linear-gradient(180deg, #cfe3ea 0%, #8fb8c8 22%, #5d8491 45%, #3f5a63 62%, #6f7f86 78%, #4a5b61 90%);
  }
  .brand {
    position: absolute; top: 74px; left: 0; width: 100%;
    display: flex; justify-content: center; align-items: center; gap: 12px;
  }
  .brand-mark { width: 30px; height: 30px; background: var(--brand-blue); }
  .brand-name { font-weight: 800; font-size: 26px; color: var(--brand-blue); letter-spacing: 0.5px; }
  .partner-logo-slot {
    position: absolute; right: 22px; top: 22px; width: 110px; height: 56px;
    border: 2px dashed rgba(255,255,255,0.85); border-radius: 6px;
  }
  .teal-disc {
    position: absolute; left: 112px; top: 222px; width: 200px; height: 200px;
    border-radius: 50%; background: var(--teal);
  }
  .display { font-family: "Anton", sans-serif; position: absolute; line-height: 1; white-space: nowrap; transform-origin: left top; }
  .headline-number {
    left: 46px; top: 210px; font-size: 320px;
    display: flex;
    transform: skewX(-10deg) scaleX(0.85);
  }
  .headline-number .digit {
    display: inline-block;
    color: var(--race-orange);
    -webkit-text-stroke: 4px #f4f4f4;
    paint-order: stroke fill;
    text-shadow: 0 6px 10px rgba(0,0,0,0.35);
  }
  .headline-word {
    left: 300px; top: 292px; font-size: 150px;
    background: linear-gradient(180deg, #ffffff 0%, #d9d9d9 45%, #9a9a9a 55%, #ffffff 100%);
    -webkit-background-clip: text; background-clip: text; color: transparent;
    filter: drop-shadow(0 4px 4px rgba(0,0,0,0.45));
    transform: skewX(-12deg) scaleX(0.86);
  }
  .headline-sub {
    left: 286px; top: 436px; font-size: 76px; color: var(--race-yellow);
    text-shadow: 0 4px 6px rgba(0,0,0,0.45);
    transform: skewX(-12deg) scaleX(0.84);
  }
  .rule-band {
    position: absolute; left: 60px; top: 566px; width: 300px; height: 46px;
    background: linear-gradient(90deg, rgba(232,90,16,0) 0%, rgba(232,90,16,0.85) 45%, var(--race-orange) 100%);
  }
  .rule-text {
    left: 70px; top: 566px; font-size: 42px; color: var(--white);
    text-shadow: 0 2px 3px rgba(0,0,0,0.4);
    transform: skewX(-10deg) scaleX(0.84);
  }
  .win-badge {
    position: absolute; left: 352px; top: 534px; width: 330px; height: 108px;
    border: 5px solid var(--race-orange); border-radius: 16px; background: var(--white);
    transform: skewX(-8deg);
  }
  .win-text {
    left: 362px; top: 528px; font-size: 112px; color: var(--ink);
    -webkit-text-stroke: 2px var(--white);
    transform: skewX(-12deg) scaleX(0.82);
  }
  .prizes {
    position: absolute; top: 714px; left: 29px; width: 680px;
    display: flex; justify-content: space-between;
  }
  .prize {
    width: 214px; height: 196px; border: 2px solid var(--teal); border-radius: 12px;
    display: flex; flex-direction: column; align-items: center; text-align: center;
    padding-top: 14px;
  }
  .prize-rank {
    font-family: "Anton", sans-serif; font-size: 44px; line-height: 1; color: var(--race-orange);
    letter-spacing: 2px; transform: skewX(-12deg);
  }
  .prize-desc { font-weight: 700; font-size: 13.5px; line-height: 1.45; margin-top: 10px; min-height: 40px; display: flex; align-items: center; }
  .prize-value { display: flex; align-items: flex-start; gap: 6px; font-weight: 800; font-size: 46px; line-height: 1; margin-top: 4px; letter-spacing: -1px; }
  .prize-value .currency { font-size: 13px; font-weight: 700; margin-top: 14px; letter-spacing: 0; }
  .prize-sponsor { font-weight: 500; font-size: 13px; margin-top: 2px; }
  .cta {
    position: absolute; top: 946px; left: 0; width: 100%; text-align: center;
    font-weight: 800; font-size: 46px; letter-spacing: 1px;
  }
  .site {
    position: absolute; top: 1012px; left: 0; width: 100%; text-align: center;
    font-weight: 700; font-size: 19px; color: var(--teal);
  }
</style>
</head>
<body>
  <main class="poster">
    <div class="track-photo" role="img" aria-label="Rennstrecke mit Tribünen unter bewölktem Himmel und rot-weissem Randstein"></div>

    <header class="brand">
      <span class="brand-mark"></span>
      <span class="brand-name">Lindauer &amp; Brack AG</span>
    </header>
    <div class="partner-logo-slot" role="img" aria-label="Platzhalter für zweites Logo"></div>

    <div class="teal-disc"></div>
    <div class="display headline-number"><span class="digit">1</span><span class="digit">5</span></div>
    <div class="display headline-word">RUNDEN</div>
    <div class="display headline-sub">SIND ZU FAHREN</div>

    <div class="rule-band"></div>
    <div class="display rule-text">DIE SCHNELLSTE ZEIT</div>
    <div class="win-badge"></div>
    <div class="display win-text">GEWINNT</div>

    <section class="prizes">
      <article class="prize">
        <h2 class="prize-rank">1PREIS</h2>
        <p class="prize-desc">Gutschein im Wert von</p>
        <p class="prize-value"><span class="currency">CHF</span>1000.-</p>
        <p class="prize-sponsor">von Vandermark</p>
      </article>
      <article class="prize">
        <h2 class="prize-rank">2PREIS</h2>
        <p class="prize-desc">Fahrzeugreinigung inkl.<br>Politur im Wert von</p>
        <p class="prize-value"><span class="currency">CHF</span>800.-</p>
      </article>
      <article class="prize">
        <h2 class="prize-rank">3PREIS</h2>
        <p class="prize-desc">Werkstatt-Gutschein<br>im Wert von</p>
        <p class="prize-value"><span class="currency">CHF</span>400.-</p>
      </article>
    </section>

    <p class="cta">JETZT MITMACHEN</p>
    <p class="site">www.lindauer-brack.ch</p>
  </main>
</body>
</html>
```